New residential property management company

I have a lot of name recognition in our smaller town due to owning a construction company here. I have now started a residential property management company representing landlords and tenants. Just trying to get my name out there and get some rentals to manage!

```html
<!DOCTYPE html>
<html lang="en">
<head>
<meta charset="utf-8">
<title>Hollin Property Management – Postcard</title>
<link rel="stylesheet" href="https://fonts.googleapis.com/css2?family=Lato:wght@400;700;900&family=Questrial&display=swap">
<style>
  :root {
    --page: #d6d6d6;
    --ink: #141414;
    --panel-dark: #1a1a1a;
    --panel-mid: #3c3c3c;
    --grey: #9b9b9b;
    --white: #ffffff;
    --red: #d91f26;
    --line: #9a9a9a;
  }
  * { box-sizing: border-box; margin: 0; padding: 0; }
  html, body { width: 902px; height: 1200px; overflow: hidden; }
  body {
    background: var(--page);
    font-family: "Lato", Arial, sans-serif;
    color: var(--ink);
    position: relative;
  }
  .side-label {
    position: absolute;
    font-weight: 900;
    font-size: 21px;
    letter-spacing: 0.5px;
    color: var(--ink);
  }
  .side-label--front { left: 718px; top: 338px; }
  .side-label--back  { left: 70px;  top: 880px; }

  .card { position: absolute; background: var(--white); overflow: hidden; }
  .card svg { position: absolute; left: 0; top: 0; }

  /* Front */
  .front { left: 105px; top: 116px; width: 579px; height: 449px; }
  .front__brand {
    position: absolute; left: 292px; top: 66px; width: 258px;
    display: flex; align-items: center; justify-content: flex-end; gap: 14px;
    color: var(--white);
  }
  .brand-mark { width: 30px; height: 30px; background: var(--white); flex: none; }
  .brand-text { text-align: right; }
  .brand-name {
    font-family: "Questrial", "Century Gothic", sans-serif;
    font-size: 44px; line-height: 1; letter-spacing: 1px;
  }
  .brand-sub {
    font-family: "Questrial", "Century Gothic", sans-serif;
    font-size: 8px; letter-spacing: 1.4px; margin-top: 4px;
  }
  .front__headline {
    position: absolute; left: 282px; top: 178px; width: 270px;
    color: var(--white); text-align: center; line-height: 1;
  }
  .headline-main { font-weight: 700; font-size: 39px; letter-spacing: 0.5px; }
  .headline-sub  { font-weight: 700; font-size: 18.5px; margin-top: 6px; letter-spacing: 0.3px; }
  .headline-end  { font-weight: 700; font-size: 44px; margin-top: 4px; letter-spacing: 0.5px; }
  .front__cta {
    position: absolute; left: 0; right: 0; top: 394px;
    display: flex; justify-content: center; align-items: center; gap: 14px;
    font-weight: 900; color: var(--ink);
  }
  .cta-label { font-size: 15px; }
  .cta-phone { display: flex; align-items: center; gap: 8px; font-weight: 700; font-size: 20px; }

  /* Back */
  .back { left: 200px; top: 641px; width: 578px; height: 449px; }
  .back__about {
    position: absolute; left: 20px; top: 30px; width: 134px; color: var(--white);
  }
  .about-title { font-weight: 700; font-size: 14px; letter-spacing: 0.3px; }
  .about-body {
    margin-top: 8px; font-weight: 700; font-size: 9.3px; line-height: 12px; text-align: justify;
  }
  .back__brand {
    position: absolute; left: 0; width: 288px; top: 238px;
    display: flex; justify-content: center; align-items: center; gap: 10px;
    color: var(--ink);
  }
  .back__brand .brand-mark { background: var(--ink); width: 28px; height: 28px; }
  .back__brand .brand-name { font-size: 34px; }
  .back__brand .brand-sub  { font-size: 6.5px; letter-spacing: 1px; }
  .back__bar {
    position: absolute; left: 0; top: 322px; width: 288px; height: 68px;
    background: var(--panel-dark); color: var(--white);
    display: flex; align-items: center; padding-left: 14px; gap: 14px;
  }
  .bar-phone { display: flex; align-items: center; gap: 8px; font-size: 15px; }
  .bar-address { display: flex; align-items: flex-start; gap: 6px; font-size: 8.5px; line-height: 10px; }
  .stamp-box {
    position: absolute; left: 475px; top: 28px; width: 81px; height: 84px;
    border: 1px solid var(--ink);
  }
  .address-line {
    position: absolute; left: 335px; width: 218px; height: 1px; background: var(--line);
  }
</style>
</head>
<body>

<div class="side-label side-label--front">FRONT</div>
<div class="side-label side-label--back">BACK</div>

<!-- Front of postcard -->
<section class="card front">
  <svg width="579" height="449" viewBox="0 0 579 449" role="img" aria-label="Photo of a two-storey suburban house with lit windows and a green lawn at dusk">
    <defs>
      <linearGradient id="housePhoto" x1="0" y1="0" x2="0" y2="1">
        <stop offset="0" stop-color="#9fbcd8"/>
        <stop offset="0.35" stop-color="#b8b2a6"/>
        <stop offset="0.62" stop-color="#9b8a72"/>
        <stop offset="0.78" stop-color="#4f7a33"/>
        <stop offset="1" stop-color="#3d6a28"/>
      </linearGradient>
    </defs>
    <rect width="579" height="449" fill="url(#housePhoto)"/>
  </svg>
  <svg width="579" height="449" viewBox="0 0 579 449" aria-hidden="true">
    <defs>
      <radialGradient id="panelShade" cx="0.55" cy="0.25" r="0.8">
        <stop offset="0" stop-color="var(--panel-mid)"/>
        <stop offset="1" stop-color="var(--panel-dark)"/>
      </radialGradient>
    </defs>
    <path class="edge-white" d="M228 0 C256 90 258 210 198 300 C150 365 70 395 0 410 L0 449 L579 449 L579 0 Z" fill="var(--white)"/>
    <path class="edge-black" d="M240 0 C268 90 268 214 210 305 C165 368 80 398 0 414 L0 449 L579 449 L579 0 Z" fill="var(--ink)"/>
    <path class="panel" d="M252 0 L579 0 L579 345 C470 330 330 330 215 345 C255 290 285 220 280 150 C276 90 266 40 252 0 Z" fill="url(#panelShade)"/>
    <path class="swoosh-grey" d="M0 392 C150 344 380 330 579 340 L579 449 L0 449 Z" fill="var(--grey)"/>
    <path class="swoosh-black" d="M0 402 C150 360 380 348 579 358 L579 449 L0 449 Z" fill="var(--ink)"/>
    <path class="band-white" d="M0 420 C150 384 380 370 579 378 L579 449 L0 449 Z" fill="var(--white)"/>
    <polygon class="burst" fill="var(--red)"
      points="201,172 214,200 240,184 238,214 270,212 252,236 278,252 248,262 262,292 230,284 222,314 204,292 182,312 176,282 146,292 158,262 128,250 156,236 140,210 170,214 170,184 192,200"/>
    <text x="204" y="236" text-anchor="middle" fill="var(--white)" font-family="Lato, sans-serif" font-weight="900" font-size="17" transform="rotate(-32 204 245)">STARTED</text>
    <text x="204" y="258" text-anchor="middle" fill="var(--white)" font-family="Lato, sans-serif" font-weight="900" font-size="17" transform="rotate(-32 204 245)">A NEW</text>
  </svg>

  <div class="front__brand">
    <span class="brand-mark"></span>
    <div class="brand-text">
      <div class="brand-name">HOLLIN</div>
      <div class="brand-sub">PROPERTY MANAGEMENT LLC.</div>
    </div>
  </div>

  <div class="front__headline">
    <div class="headline-main">RESIDENTIAL</div>
    <div class="headline-sub">PROPERTY MANAGEMENT</div>
    <div class="headline-end">COMPANY</div>
  </div>

  <div class="front__cta">
    <span class="cta-label">CALL ME TODAY!</span>
    <span class="cta-phone">
      <svg width="22" height="22" viewBox="0 0 22 22" aria-hidden="true" style="position:static">
        <circle cx="11" cy="11" r="9.5" fill="none" stroke="var(--ink)" stroke-width="1.6"/>
        <path d="M7.5 6.5 L9 6 L10 8.5 L9 9.5 C9.6 11 10.8 12.3 12.5 13 L13.5 12 L16 13 L15.5 14.6 C11 15 7 11 7.5 6.5 Z" fill="var(--ink)"/>
      </svg>
      123-456-7890
    </span>
  </div>
</section>

<!-- Back of postcard -->
<section class="card back">
  <svg width="288" height="215" viewBox="0 0 288 215" role="img" aria-label="Photo of a red For Rent sign on a post in front of a suburban house">
    <defs>
      <linearGradient id="rentPhoto" x1="0" y1="0" x2="1" y2="1">
        <stop offset="0" stop-color="#9a9c9c"/>
        <stop offset="0.5" stop-color="#8e8a84"/>
        <stop offset="0.75" stop-color="#b53a3f"/>
        <stop offset="1" stop-color="#5f7a4a"/>
      </linearGradient>
    </defs>
    <rect width="288" height="215" fill="url(#rentPhoto)"/>
  </svg>
  <svg width="578" height="449" viewBox="0 0 578 449" aria-hidden="true">
    <rect class="about-overlay" x="0" y="0" width="165" height="215" fill="var(--panel-dark)" opacity="0.72"/>
    <path class="photo-curve" d="M0 205 C70 170 130 220 200 195 C240 182 265 180 288 186 L288 240 L0 240 Z" fill="var(--white)"/>
    <path class="photo-curve-shade" d="M0 210 C70 178 130 226 200 201 C240 188 265 186 288 192" fill="none" stroke="#d4d4d4" stroke-width="5"/>
    <rect class="panel-edge" x="288" y="0" width="6" height="390" fill="#c9c9c9"/>
  </svg>

  <div class="back__about">
    <h2 class="about-title">ABOUT US</h2>
    <p class="about-body">Lorem Ipsum is simply dummy text of the printing and type­setting industry. Lorem Ipsum has been the industry's stand­ard dummy text ever since the 1500s, when an unknown printer took a galley of type and scrambled it to make a type specimen book.</p>
  </div>

  <div class="back__brand">
    <span class="brand-mark"></span>
    <div>
      <div class="brand-name">HOLLIN</div>
      <div class="brand-sub" style="text-align:right">PROPERTY MANAGEMENT LLC.</div>
    </div>
  </div>

  <div class="back__bar">
    <span class="bar-phone">
      <svg width="10" height="10" viewBox="0 0 22 22" aria-hidden="true" style="position:static">
        <circle cx="11" cy="11" r="9.5" fill="none" stroke="var(--white)" stroke-width="2"/>
        <path d="M7.5 6.5 L9 6 L10 8.5 L9 9.5 C9.6 11 10.8 12.3 12.5 13 L13.5 12 L16 13 L15.5 14.6 C11 15 7 11 7.5 6.5 Z" fill="var(--white)"/>
      </svg>
      123-456-7890
    </span>
    <span class="bar-address">
      <svg width="8" height="11" viewBox="0 0 8 11" aria-hidden="true" style="position:static">
        <path d="M4 0 C6.2 0 8 1.7 8 3.9 C8 6.5 4 11 4 11 C4 11 0 6.5 0 3.9 C0 1.7 1.8 0 4 0 Z" fill="var(--white)"/>
        <circle cx="4" cy="3.9" r="1.5" fill="var(--panel-dark)"/>
      </svg>
      <span>Hollin Property Management<br>Your company address</span>
    </span>
  </div>

  <div class="stamp-box"></div>
  <div class="address-line" style="top:202px"></div>
  <div class="address-line" style="top:247px"></div>
  <div class="address-line" style="top:292px"></div>
</section>

</body>
</html>
```